Exercise Physiologist needs a Brochure

I am Exercise Physiologist providing exercise therapy for a variety of conditions. I have a logo and recent business card design. I like the black background like the front of the business cards. I have attached the flyer information required. I have also attached a few photos however they do not have to be used, happy to have no photos at all.

Industry/Entity Type

Health And Wellness

Font styles to use
Sans Serif

Requirements
Must have
• Please also add instagram @varnolhealth
Nice to have
• tri-fold brochure

```html
<!DOCTYPE html>
<html lang="en">
<head>
<meta charset="utf-8">
<title>Varnol Health &amp; Rehabilitation – Tri-fold Brochure</title>
<link href="https://fonts.googleapis.com/css2?family=Open+Sans:wght@400;600;700;800&display=swap" rel="stylesheet">
<style>
  :root{
    --ink:#232323;
    --blue:#1e9be0;
    --blue-strong:#1463c4;
    --navy:#0b3a6e;
    --sky:#3aa8e8;
    --text-light:#f2f2f2;
    --text-dark:#222;
    --bg:#eceeef;
  }
  *{box-sizing:border-box;margin:0;padding:0}
  html,body{width:820px;height:1200px;overflow:hidden;background:var(--bg)}
  body{font-family:"Open Sans",Arial,sans-serif;color:var(--text-light)}
  .canvas{position:relative;width:820px;height:1200px;overflow:hidden}
  .sheet{position:absolute;left:10px;width:800px;height:565px;overflow:hidden;box-shadow:0 4px 14px rgba(0,0,0,.25)}
  .sheet--outside{top:20px}
  .sheet--inside{top:615px}
  .sheet__art{position:absolute;inset:0;width:800px;height:565px}
  .abs{position:absolute}

  .kicker{font-size:22px;font-weight:400;line-height:1.1;color:var(--text-light)}
  .headline{font-weight:800;color:var(--blue);text-transform:uppercase;line-height:1.1}
  .rule{width:22px;height:3px;background:var(--blue);margin:8px 0 12px}
  .body-copy{font-size:10.6px;line-height:1.42;text-align:justify}

  .phone-big{font-size:25px;font-weight:700;color:#fff;display:flex;align-items:center;gap:8px;letter-spacing:.5px}
  .icon{display:inline-block;flex:none}

  .contact{left:267px;width:266px;text-align:center;color:var(--text-dark)}
  .contact__cta{font-size:14px;font-weight:700;line-height:1.3}
  .contact__cta strong{display:block;font-size:24px;font-weight:800;color:var(--blue-strong);line-height:1.2}
  .contact__line{display:flex;align-items:center;justify-content:center;gap:6px}

  .brand{display:flex;align-items:center;gap:8px}
  .brand__dot{width:50px;height:50px;border-radius:50%;border:4px solid var(--blue-strong)}
  .brand__name{font-size:30px;font-weight:700;color:var(--blue-strong);line-height:1}
  .brand__sub{font-size:8px;font-weight:600;color:var(--blue-strong);letter-spacing:.5px}

  .band-title{font-size:24px;line-height:1.1;color:#fff}
  .band-title b{font-weight:800;text-transform:uppercase}

  .name{font-size:27px;font-weight:400;color:var(--blue);line-height:1.2}
  .name b{font-weight:700}
  .role{font-size:16px;color:#fff}
  .creds{font-size:11px;line-height:1.45;color:#fff}
  .tagline{font-size:18px;color:#fff;font-weight:400}
  .tagline b{color:var(--blue);font-weight:700}
  .quote-mark{font-size:50px;font-weight:800;color:#cfcfcf;line-height:1}
  .quote{font-size:9.4px;line-height:1.42;color:#fff}

  .help-copy{font-size:9.2px;line-height:1.45;color:var(--text-dark);text-align:justify}
  .help-copy p{margin-bottom:7px}

  .conditions-title{font-size:14px;color:#fff;line-height:1.35}
  .conditions-title b{color:var(--blue);font-weight:700;display:block}
  .conditions{list-style:none;font-size:10.5px;font-weight:700;color:#fff;line-height:1.3}
  .conditions li{position:relative;padding-left:14px;margin-bottom:4px}
  .conditions li::before{content:"";position:absolute;left:0;top:4px;width:7px;height:7px;border-radius:50%;background:var(--blue)}
  .small-copy{font-size:9px;line-height:1.42;color:#fff}

  .portrait-slot{text-align:left;font-size:12px;font-weight:600;color:#fff;line-height:1.4}
</style>
</head>
<body>
<div class="canvas">

  <section class="sheet sheet--outside">
    <svg class="sheet__art" viewBox="0 0 800 565">
      <defs>
        <linearGradient id="midPanel" x1="0" y1="0" x2="0" y2="1">
          <stop offset="0" stop-color="#ffffff"/><stop offset="1" stop-color="#dfe1e3"/>
        </linearGradient>
        <linearGradient id="kneeTone" x1="0" y1="0" x2="1" y2="1">
          <stop offset="0" stop-color="#d9d9d9"/><stop offset=".5" stop-color="#b9b4b2"/><stop offset="1" stop-color="#8a8685"/>
        </linearGradient>
        <linearGradient id="gymTone" x1="0" y1="0" x2="1" y2="1">
          <stop offset="0" stop-color="#c9e4e8"/><stop offset=".6" stop-color="#4d7f88"/><stop offset="1" stop-color="#1e3a40"/>
        </linearGradient>
        <linearGradient id="poseTone" x1="0" y1="0" x2="0" y2="1">
          <stop offset="0" stop-color="#d6e6f3"/><stop offset="1" stop-color="#f3f6f9"/>
        </linearGradient>
      </defs>
      <rect x="0" y="0" width="267" height="565" fill="var(--ink)"/>
      <rect x="267" y="0" width="266" height="565" fill="url(#midPanel)"/>
      <rect x="533" y="0" width="267" height="565" fill="var(--ink)"/>

      <rect x="533" y="160" width="267" height="260" fill="url(#kneeTone)" role="img" aria-label="Photo: hands holding a sore knee"/>
      <path d="M533,205 Q640,150 800,135 L800,160 Q650,172 533,225 Z" fill="#ffffff"/>
      <path d="M533,190 Q640,140 800,118 L800,140 Q650,158 533,210 Z" fill="var(--blue-strong)"/>
      <path d="M533,478 Q555,400 650,390 L800,372 L800,460 Q700,476 600,482 Z" fill="var(--blue-strong)"/>

      <rect x="300" y="34" width="200" height="165" rx="6" fill="url(#poseTone)" role="img" aria-label="Illustration: silhouette of a woman holding a side plank"/>

      <path d="M0,370 Q130,330 260,420 Q420,560 800,475" fill="none" stroke="var(--blue-strong)" stroke-width="14"/>
      <path d="M0,455 Q330,575 800,480 L800,565 L0,565 Z" fill="var(--ink)"/>
      <path d="M0,446 Q330,566 800,472" fill="none" stroke="#ffffff" stroke-width="6"/>
      <path d="M0,434 Q330,554 800,464" fill="none" stroke="var(--blue)" stroke-width="6"/>

      <circle cx="140" cy="405" r="100" fill="var(--blue-strong)"/>
      <circle cx="140" cy="405" r="88" fill="url(#gymTone)" role="img" aria-label="Photo: racks of dumbbells in a gym"/>

      <line x1="267" y1="0" x2="267" y2="565" stroke="rgba(0,0,0,.12)"/>
      <line x1="533" y1="0" x2="533" y2="565" stroke="rgba(0,0,0,.12)"/>
    </svg>

    <div class="abs" style="left:31px;top:35px;width:210px">
      <div class="kicker">What is an</div>
      <div class="headline" style="font-size:24px">Exercise<br>Physiologist?</div>
      <div class="rule"></div>
      <p class="body-copy">Exercise Physiologists are university educated health professionals trained to provide exercise therapy for pain and injury, pre and post surgery, mental health and chronic disease. They are registered providers with RoadCare, JobShield, PublicCare and Veterans Services Office and many Private Health funds.</p>
    </div>

    <div class="abs phone-big" style="left:36px;top:518px">
      <svg class="icon" width="22" height="22" viewBox="0 0 22 22"><circle cx="11" cy="11" r="9.5" fill="none" stroke="var(--blue)" stroke-width="2"/><path d="M7.5 6.5l2 0 1 3-1.3 1a6 6 0 0 0 2.8 2.8l1-1.3 3 1v2c0 .6-.5 1-1 1A9 9 0 0 1 6.5 7.5c0-.5.4-1 1-1z" fill="var(--blue)"/></svg>
      0400 555 182
    </div>

    <div class="abs contact" style="top:210px">
      <p class="contact__cta">CALL OR EMAIL ME TODAY<br>TO SEE HOW<strong>I CAN HELP YOU</strong></p>
      <div style="margin:10px auto 5px;width:22px">
        <svg width="22" height="22" viewBox="0 0 22 22"><circle cx="11" cy="11" r="10" fill="none" stroke="var(--blue-strong)" stroke-width="1.2"/><path d="M11 5a3.5 3.5 0 0 0-3.5 3.5C7.5 11 11 16 11 16s3.5-5 3.5-7.5A3.5 3.5 0 0 0 11 5z" fill="none" stroke="var(--blue-strong)" stroke-width="1.2"/><circle cx="11" cy="8.5" r="1.2" fill="var(--blue-strong)"/></svg>
      </div>
      <p style="font-size:10.5px;line-height:1.45">Gate 4, 18 Quarry Lane NORTHBANK<br>(Halden Fitness)</p>
      <p class="contact__line" style="font-size:14px;font-weight:700;margin-top:9px">
        <svg class="icon" width="14" height="14" viewBox="0 0 22 22"><circle cx="11" cy="11" r="9.5" fill="none" stroke="var(--blue-strong)" stroke-width="2"/><path d="M7.5 6.5l2 0 1 3-1.3 1a6 6 0 0 0 2.8 2.8l1-1.3 3 1v2c0 .6-.5 1-1 1A9 9 0 0 1 6.5 7.5c0-.5.4-1 1-1z" fill="var(--blue-strong)"/></svg>
        0400 555 182</p>
      <p class="contact__line" style="font-size:12.5px;margin-top:7px">
        <svg class="icon" width="13" height="10" viewBox="0 0 13 10"><rect x=".6" y=".6" width="11.8" height="8.8" fill="none" stroke="var(--blue-strong)" stroke-width="1.2"/><path d="M.6.6l5.9 5 5.9-5" fill="none" stroke="var(--blue-strong)" stroke-width="1.2"/></svg>
        varnolhealth@mail.com</p>
      <p class="contact__line" style="font-size:9px;margin-top:14px"><span class="icon" style="width:16px;height:16px;border-radius:50%;background:var(--blue-strong)"></span>facebook.com/Varnol</p>
      <p class="contact__line" style="font-size:9px;margin-top:8px"><span class="icon" style="width:16px;height:16px;border-radius:50%;background:#d8336b"></span>@varnolhealth</p>
    </div>

    <div class="abs brand" style="left:560px;top:30px">
      <span class="brand__dot"></span>
      <div><div class="brand__name">varnol</div><div class="brand__sub">HEALTH &amp; REHABILITATION</div></div>
    </div>

    <div class="abs band-title" style="left:610px;top:398px">Heal through<br><b>Movement</b></div>

    <div class="abs phone-big" style="left:568px;top:518px">
      <svg class="icon" width="22" height="22" viewBox="0 0 22 22"><circle cx="11" cy="11" r="9.5" fill="none" stroke="var(--blue)" stroke-width="2"/><path d="M7.5 6.5l2 0 1 3-1.3 1a6 6 0 0 0 2.8 2.8l1-1.3 3 1v2c0 .6-.5 1-1 1A9 9 0 0 1 6.5 7.5c0-.5.4-1 1-1z" fill="var(--blue)"/></svg>
      0400 555 182
    </div>
  </section>

  <section class="sheet sheet--inside">
    <svg class="sheet__art" viewBox="0 0 800 565">
      <defs>
        <linearGradient id="topBlue" x1="0" y1="0" x2="1" y2="0">
          <stop offset="0" stop-color="#1c7fd0"/><stop offset="1" stop-color="var(--sky)"/>
        </linearGradient>
        <linearGradient id="helpPanel" x1="0" y1="0" x2="0" y2="1">
          <stop offset="0" stop-color="#c8dfec"/><stop offset="1" stop-color="#eef4f8"/>
        </linearGradient>
        <linearGradient id="runTone" x1="0" y1="0" x2="0" y2="1">
          <stop offset="0" stop-color="#e9eef2"/><stop offset=".55" stop-color="#b9cbd6"/><stop offset=".75" stop-color="#3f7fa8"/><stop offset="1" stop-color="#2a5f84"/>
        </linearGradient>
        <linearGradient id="grassTone" x1="0" y1="0" x2="0" y2="1">
          <stop offset="0" stop-color="#6d7a5a"/><stop offset="1" stop-color="#3e6b2c"/>
        </linearGradient>
      </defs>
      <rect width="800" height="565" fill="var(--ink)"/>
      <rect x="267" y="30" width="266" height="535" fill="url(#helpPanel)"/>
      <rect x="267" y="300" width="266" height="230" fill="url(#runTone)" role="img" aria-label="Photo: a woman and a man jogging along the seaside"/>
      <path d="M0,0 L800,0 L800,42 Q330,0 0,100 Z" fill="url(#topBlue)"/>
      <path d="M0,100 Q330,0 800,42" fill="none" stroke="#ffffff" stroke-width="6"/>
      <path d="M0,112 Q330,12 800,54" fill="none" stroke="var(--blue-strong)" stroke-width="4" opacity=".8"/>

      <path d="M640,30 Q790,40 790,160 Q780,220 720,225" fill="none" stroke="var(--blue-strong)" stroke-width="8"/>
      <circle cx="680" cy="112" r="80" fill="var(--blue-strong)"/>
      <circle cx="680" cy="112" r="70" fill="url(#grassTone)" role="img" aria-label="Photo: legs of a runner in trainers on grass"/>

      <path d="M0,430 Q120,380 260,440" fill="none" stroke="var(--blue-strong)" stroke-width="16"/>
      <path d="M0,485 Q400,610 800,525 L800,565 L0,565 Z" fill="var(--navy)"/>
      <path d="M0,478 Q400,603 800,518" fill="none" stroke="#ffffff" stroke-width="5"/>
      <path d="M0,468 Q400,592 800,508" fill="none" stroke="var(--blue)" stroke-width="5"/>

      <circle cx="110" cy="490" r="78" fill="none" stroke="var(--blue-strong)" stroke-width="8"/>
      <circle cx="110" cy="490" r="68" fill="#5aaee6" role="img" aria-label="Portrait photo of Maren Lowry goes here"/>

      <line x1="267" y1="0" x2="267" y2="565" stroke="rgba(0,0,0,.12)"/>
      <line x1="533" y1="0" x2="533" y2="565" stroke="rgba(0,0,0,.12)"/>
    </svg>

    <div class="abs" style="left:35px;top:118px;width:220px">
      <div class="name">Maren <b>Lowry</b></div>
      <div class="role">Exercise Physiologist</div>
      <div style="width:22px;height:3px;background:var(--blue);margin:8px 0 10px"></div>
      <p class="creds">B.AppSci – Human Mvmt<br>Grad Dip – ExRehab<br>Cert IV – Training &amp; Assessment</p>
      <p class="tagline" style="margin-top:12px">Heal <b>through Movement</b></p>
      <div class="quote-mark" style="margin-top:6px;height:30px">&ldquo;</div>
      <p class="quote" style="width:200px">Don't let the right exercise but the wrong technique hinder your recovery. Discover how important the correct exercise technique is to your success</p>
      <div class="quote-mark" style="text-align:right;margin-right:10px;height:30px">&rdquo;</div>
    </div>
    <div class="abs portrait-slot" style="left:105px;top:453px">Maren Lowry<br>Image Here</div>

    <div class="abs" style="left:294px;top:56px;width:212px">
      <div class="kicker" style="color:var(--text-dark)">How can</div>
      <div class="headline" style="font-size:22px;color:var(--blue-strong)">I Help You?</div>
      <div class="rule"></div>
      <div class="help-copy">
        <p>I have over 13 years of experience working as an Exercise Physiologist and have been working in the sport and fitness industry since 1996. I understand that everyone's health and exercise experience is unique and will tailor a program to suit you and your lifestyle.</p>
        <p>Managing your condition involves working with you to develop the best exercises and teaching you the correct technique essential to improve. Home and gym based programs can be provided.</p>
        <p>When appropriate I can also work with your current treating health practitioner to provide a holistic approach to your recovery.</p>
      </div>
    </div>

    <div class="abs" style="left:560px;top:200px;width:230px">
      <p class="conditions-title">Common conditions that<b>benefit from exercise therapy</b></p>
      <ul class="conditions" style="margin-top:10px">
        <li>Back pain</li>
        <li>Joint pain</li>
        <li>Pain relating to exercise</li>
        <li>Arthritis</li>
        <li>Anxiety relating to exercise</li>
        <li>Depression and Anxiety</li>
        <li>Chronic diseases such as diabetes, heart and lung disease.</li>
        <li>Motor vehicle accidents</li>
      </ul>
      <p class="small-copy" style="margin-top:8px">Performing the right exercise the wrong way can do more harm than good. I can teach you what, how and when to perform your tailored exercise program to get the best results.</p>
    </div>
  </section>

</div>
</body>
</html>
```